Cover for Where the Quiet River Bends Beyond Our Morning

Cover for a book that describes everything that happens to a person, from pre-birth life plans through growing in compassion and wisdom to death and living in the afterlife. The information is revealed in messages from people living in the life after this life. The title is Lanterns Along the Hidden Stair of Every Soul: Gathered from Voices Dwelling in the Further Meadow. Author is T. Morven Ashdale. Book size is 6 by 9.

Target Market(s)

General

Font styles to use
Serif

```html
<!DOCTYPE html>
<html lang="en">
<head>
<meta charset="utf-8">
<title>Lanterns Along the Hidden Stair of Every Soul — T. Morven Ashdale</title>
<link rel="stylesheet" href="https://fonts.googleapis.com/css2?family=Alfa+Slab+One&family=Lilita+One&display=swap">
<style>
  :root {
    --maroon: #4d2a2e;
    --deep-red: #8f1f24;
    --ember: #c8452a;
    --gold: #d9a62a;
    --glow-green: #4f9a3c;
    --olive: #8a8f2e;
    --ink-shadow: #2a1416;
    --paper: #ffffff;
  }
  * { margin: 0; padding: 0; box-sizing: border-box; }
  html, body {
    width: 857px; height: 1200px; overflow: hidden;
    background: var(--maroon);
  }
  .cover {
    position: relative;
    width: 857px; height: 1200px;
    overflow: hidden;
    color: var(--paper);
  }
  .cover__sky {
    position: absolute; inset: 0;
    background:
      radial-gradient(ellipse 70% 28% at 50% 80%, rgba(77,42,46,0.95) 0%, rgba(77,42,46,0) 100%),
      radial-gradient(ellipse 45% 18% at 30% 70%, rgba(217,166,42,0.75) 0%, rgba(217,166,42,0) 100%),
      radial-gradient(ellipse 55% 30% at 60% 64%, rgba(79,154,60,0.8) 0%, rgba(79,154,60,0) 100%),
      radial-gradient(ellipse 40% 12% at 70% 99%, rgba(200,69,42,0.8) 0%, rgba(200,69,42,0) 100%),
      radial-gradient(ellipse 60% 40% at 20% 10%, rgba(143,31,36,0.7) 0%, rgba(143,31,36,0) 100%),
      linear-gradient(180deg, #5a2a2c 0%, #4e2a2e 40%, #5b4a2c 62%, #4d2a2e 100%);
  }
  .cover__author {
    position: absolute; top: 62px; left: 0; right: 0;
    text-align: center;
    font-family: "Alfa Slab One", serif;
    font-size: 38px;
    letter-spacing: 0.42em;
    padding-left: 0.42em;
  }
  .cover__title {
    position: absolute; top: 150px; left: 0; right: 0;
    text-align: center;
    font-family: "Lilita One", sans-serif;
    text-transform: uppercase;
    text-shadow: 3px 4px 0 var(--ink-shadow);
    line-height: 1;
  }
  .cover__title-main { display: block; font-size: 138px; letter-spacing: 0.01em; }
  .cover__title-sub { display: block; font-size: 50px; margin-top: 14px; }
  .cover__title-sub--large { font-size: 74px; margin-top: 8px; }
  .cover__tagline {
    position: absolute; left: 89px; top: 985px;
    width: 694px; height: 80px;
  }
  .cover__tagline-frame { position: absolute; inset: 0; }
  .cover__tagline-text {
    position: absolute; left: 0; right: 0; top: 14px;
    text-align: center;
    font-family: "Lilita One", sans-serif;
    font-size: 33px; line-height: 45px;
    text-transform: uppercase;
    text-shadow: 2px 2px 0 var(--ink-shadow);
  }
</style>
</head>
<body>
  <main class="cover">
    <div class="cover__sky" role="img" aria-label="Photograph of rays of green and golden light bursting through dark storm clouds in a red sky"></div>

    <p class="cover__author">T. MORVEN ASHDALE</p>

    <h1 class="cover__title">
      <span class="cover__title-main">Lanterns</span>
      <span class="cover__title-sub">Along the Hidden Stair</span>
      <span class="cover__title-sub cover__title-sub--large">of Every Soul</span>
    </h1>

    <div class="cover__tagline">
      <svg class="cover__tagline-frame" width="694" height="80" viewBox="0 0 694 80" aria-hidden="true">
        <polyline points="122,78.5 1.5,78.5 1.5,1.5 692.5,1.5 692.5,78.5 574,78.5"
                  fill="none" stroke="#ffffff" stroke-width="3"/>
      </svg>
      <p class="cover__tagline-text">Gathered from Voices Dwelling<br>in the Further Meadow</p>
    </div>
  </main>
</body>
</html>
```